Oro Raffle Header Design

For a future Lottery website (Oro Raffle)

We need a Header of 950 x 125 pix

The 'B' will be a bitcoin sign

Any colors you like, The header should communicate a possibility of getting wealthy

*EDIT* : We want to have "What is Oro Raffle ?" and "Register Here" in the header, it will be links so it has to be obvious that we can click on it

Logo Text

Oro Raffle

```html
<!DOCTYPE html>
<html lang="en">
<head>
<meta charset="utf-8">
<title>Oro Raffle Header</title>
<link rel="stylesheet" href="https://fonts.googleapis.com/css2?family=Tinos:wght@400;700&display=swap">
<style>
  :root {
    --bg-dark: #141414;
    --bg-mid: #2b2b2b;
    --ribbon-red: #b3121a;
    --ribbon-deep: #6e0a0e;
    --gold-light: #f6dc8a;
    --gold: #d6a93c;
    --gold-deep: #8a6220;
    --button-fill: #050505;
    --button-ring: #c9c9c9;
    --button-ring-dark: #5a5a5a;
    --button-text: #f2f2f2;
  }
  * { margin: 0; padding: 0; box-sizing: border-box; }
  html, body { width: 1200px; height: 159px; overflow: hidden; background: var(--bg-dark); }
  .header {
    position: relative;
    width: 1200px;
    height: 159px;
    overflow: hidden;
    background: radial-gradient(ellipse at 50% 50%, var(--bg-mid) 0%, var(--bg-dark) 75%);
    font-family: "Tinos", "Times New Roman", serif;
  }
  .damask-pattern {
    position: absolute; inset: 0;
    background: radial-gradient(ellipse at 35% 40%, #333 0%, transparent 45%),
                radial-gradient(ellipse at 75% 60%, #2e2e2e 0%, transparent 45%);
  }
  .ribbon {
    position: absolute; left: 0; top: 10px; width: 580px; height: 140px;
  }
  .brand {
    position: absolute; left: 128px; top: 38px;
    display: flex; align-items: center; gap: 14px;
    color: var(--gold-light);
    font-size: 68px; font-weight: 400; line-height: 1;
  }
  .brand-mark {
    width: 34px; height: 34px; border-radius: 50%;
    background: var(--gold);
  }
  .crown-flourish {
    position: absolute; left: 748px; top: 0; width: 312px; height: 72px;
  }
  .corner-curl { position: absolute; top: 0; }
  .corner-curl--left { left: 0; }
  .corner-curl--right { right: 0; }
  .nav-link {
    position: absolute; top: 82px; height: 70px;
    display: flex; align-items: center; justify-content: center;
    border-radius: 35px;
    background: linear-gradient(180deg, #2a2a2a 0%, var(--button-fill) 50%, #000 100%);
    border: 4px solid var(--button-ring);
    box-shadow: 0 0 0 2px var(--button-ring-dark), inset 0 2px 3px rgba(255,255,255,.25);
    color: var(--button-text);
    font-size: 24px; text-decoration: none; letter-spacing: .3px;
  }
  .nav-link--about { left: 660px; width: 256px; }
  .nav-link--register { left: 930px; width: 250px; }
</style>
</head>
<body>
<header class="header">
  <div class="damask-pattern" role="img" aria-label="Dark grey damask wallpaper pattern"></div>

  <svg class="ribbon" viewBox="0 0 580 140" role="img" aria-label="Flowing red satin ribbon behind the brand name">
    <defs>
      <linearGradient id="ribbonFill" x1="0" y1="0" x2="0" y2="1">
        <stop offset="0" stop-color="#d42028"/>
        <stop offset="1" stop-color="#6e0a0e"/>
      </linearGradient>
    </defs>
    <path d="M0 30 C120 0 250 10 360 30 C450 45 520 30 580 20 L560 110 C480 120 420 100 330 95 C220 90 110 120 0 115 Z" fill="url(#ribbonFill)"/>
  </svg>

  <div class="brand">
    <span class="brand-mark"></span>
    <span class="brand-name">Oro Raffle</span>
  </div>

  <svg class="crown-flourish" viewBox="0 0 312 72" role="img" aria-label="Golden crown above an ornamental gold flourish">
    <defs>
      <linearGradient id="goldFill" x1="0" y1="0" x2="0" y2="1">
        <stop offset="0" stop-color="#f6dc8a"/>
        <stop offset="1" stop-color="#8a6220"/>
      </linearGradient>
    </defs>
    <rect x="112" y="2" width="96" height="52" rx="8" fill="url(#goldFill)" opacity=".9"/>
    <rect x="0" y="52" width="312" height="14" rx="7" fill="url(#goldFill)" opacity=".85"/>
  </svg>

  <svg class="corner-curl corner-curl--left" width="88" height="60" viewBox="0 0 88 60">
    <path d="M0 0 H88 C60 10 30 30 0 60 Z" fill="var(--gold)"/>
    <path d="M0 0 H88 C50 4 20 20 0 48 Z" fill="var(--gold-light)"/>
  </svg>
  <svg class="corner-curl corner-curl--right" width="88" height="60" viewBox="0 0 88 60">
    <path d="M88 0 H0 C28 10 58 30 88 60 Z" fill="var(--gold)"/>
    <path d="M88 0 H0 C38 4 68 20 88 48 Z" fill="var(--gold-light)"/>
  </svg>

  <a class="nav-link nav-link--about" href="#about">What is Oro Raffle ?</a>
  <a class="nav-link nav-link--register" href="#register">Register Here</a>
</header>
</body>
</html>
```